Business card for auto dealership

Looking for a clean modern design.
Would like attached logo incorporated

Industry/Entity Type

Car dealership

Contact Information for Business Card

Name, website, phone, cell, fax, email

```html
<!DOCTYPE html>
<html lang="en">
<head>
<meta charset="utf-8">
<title>Harlow Truck &amp; Auto Sales — Business Card</title>
<link rel="stylesheet" href="https://fonts.googleapis.com/css2?family=Poppins:wght@400;500;600;700&display=swap">
<style>
  :root {
    --red: #dc2222;
    --yellow: #e6e025;
    --white: #ffffff;
    --ink: #1c1c1c;
    --grey: #4a4a4a;
    --stage: #2b2f36;
  }
  * { margin: 0; padding: 0; box-sizing: border-box; }
  html, body {
    width: 1200px; height: 780px; overflow: hidden;
    background: var(--stage);
    font-family: "Poppins", sans-serif;
  }
  .sheet {
    position: relative; width: 1200px; height: 780px;
    display: flex; align-items: center; justify-content: center; gap: 48px;
  }
  .card {
    position: relative; width: 540px; height: 310px;
    border-radius: 18px; overflow: hidden; background: var(--white);
    box-shadow: 0 12px 30px rgba(0,0,0,.45);
  }

  /* Front */
  .front { background: var(--red); }
  .front .base-band {
    position: absolute; left: 0; right: 0; bottom: 0; height: 58px;
    background: var(--white); border-top: 9px solid var(--yellow);
  }
  .front .email-pill {
    position: absolute; left: 80px; bottom: 30px; width: 290px; height: 46px;
    border-radius: 23px; background: var(--yellow);
    outline: 8px solid var(--red);
    display: flex; align-items: center; justify-content: center;
    font-weight: 600; font-size: 19px; color: var(--ink);
  }
  .wordmark { color: var(--yellow); font-weight: 700; text-align: center; line-height: 1; }
  .front .wordmark { position: absolute; left: 0; right: 0; top: 78px; }
  .front .wordmark .name { font-size: 74px; letter-spacing: 1px; }
  .front .wordmark .tag { font-size: 15px; letter-spacing: 3px; margin-top: 6px; }

  /* Back */
  .back .brand-side {
    position: absolute; left: 0; top: 0; bottom: 0; width: 290px;
    background: var(--red); border-right: 9px solid var(--yellow);
  }
  .back .edge-tab {
    position: absolute; left: -14px; top: 28px; width: 28px; height: 120px;
    border-radius: 14px; background: var(--yellow);
  }
  .back .wordmark { position: absolute; left: 30px; top: 64px; width: 230px; text-align: center; }
  .back .wordmark .name { font-size: 50px; }
  .back .wordmark .tag { font-size: 10px; letter-spacing: 2px; margin-top: 5px; }
  .back .icon-pill {
    position: absolute; left: 268px; top: 140px; width: 40px; height: 150px;
    border-radius: 20px; background: var(--yellow); outline: 7px solid var(--red);
    display: flex; flex-direction: column; align-items: center; justify-content: space-evenly;
    padding: 8px 0;
  }
  .icon-pill svg { width: 17px; height: 17px; fill: var(--ink); }
  .back .details { position: absolute; left: 322px; top: 36px; right: 16px; }
  .back .person { color: var(--red); font-weight: 500; font-size: 25px; letter-spacing: .5px; line-height: 1.1; }
  .back .role { color: var(--grey); font-size: 11px; letter-spacing: 4px; margin-top: 4px; }
  .back .contacts { list-style: none; margin-top: 22px; }
  .back .contacts li { font-size: 14px; color: var(--ink); height: 34px; line-height: 34px; }
  .back .corner-block {
    position: absolute; right: -30px; bottom: -30px; width: 150px; height: 90px;
    border-radius: 26px; background: var(--red);
  }
</style>
</head>
<body>
<main class="sheet">
  <section class="card front" aria-label="Card front">
    <div class="wordmark">
      <div class="name">Harlow</div>
      <div class="tag">TRUCK &amp; AUTO SALES</div>
    </div>
    <div class="base-band"></div>
    <div class="email-pill">dana@harlowauto.com</div>
  </section>

  <section class="card back" aria-label="Card back">
    <div class="brand-side">
      <div class="edge-tab"></div>
      <div class="wordmark">
        <div class="name">Harlow</div>
        <div class="tag">TRUCK &amp; AUTO SALES</div>
      </div>
    </div>
    <div class="icon-pill">
      <svg viewBox="0 0 24 24" aria-label="Office phone"><path d="M3 9c0-3 4-5 9-5s9 2 9 5v2h-5V8.5c-1.3-.5-2.6-.7-4-.7s-2.7.2-4 .7V11H3zM6 12h12l2 8H4zm6 2.5a2.5 2.5 0 1 0 0 5 2.5 2.5 0 0 0 0-5z"/></svg>
      <svg viewBox="0 0 24 24" aria-label="Mobile"><path d="M6.6 10.8c1.4 2.8 3.8 5.1 6.6 6.6l2.2-2.2c.3-.3.7-.4 1-.2 1.1.4 2.3.6 3.6.6.6 0 1 .4 1 1V20c0 .6-.4 1-1 1C10.6 21 3 13.4 3 4c0-.6.4-1 1-1h3.5c.6 0 1 .4 1 1 0 1.3.2 2.5.6 3.6.1.3 0 .7-.2 1z"/></svg>
      <svg viewBox="0 0 24 24" aria-label="Fax"><path d="M6 2h9l3 3v5H6zM3 11h18v9H3zm3 3v2h4v-2zm9 0v2h3v-2z"/></svg>
      <svg viewBox="0 0 24 24" aria-label="Email"><path d="M2 21 23 12 2 3v7l15 2-15 2z"/></svg>
    </div>
    <div class="details">
      <h1 class="person">DANA HARLOW</h1>
      <p class="role">CEO/FOUNDER</p>
      <ul class="contacts">
        <li>555-010-2368</li>
        <li>555-010-7493</li>
        <li>555-010-3857</li>
        <li>dana@harlowauto.com</li>
      </ul>
    </div>
    <div class="corner-block"></div>
  </section>
</main>
</body>
</html>
```